Design a Retail Box for Industrial Welding Helmets

We are excited to launch a design contest for our product's new retail packaging.
The products are 2 welding helmets.
Product 1 is Brontal helmet and product 2 is Veltrix helmet.
We are seeking for :
A) 1 main design of the box with minor adjustments for the 2 different models (Brontal and Veltrix)
B) 1 design for the sticker of Brontal (font)
C)1 design for the sticker of Veltrix (font)
Attached you will find:
1)Brand logo
2)Reference of welding wire packaging
3)Reference of welding torch packaging
4)Photo of Brontal model
5)Data of Brontal model to be included
6)Photo of Veltrix model
7)Data of Veltrix model to be included
8)Dieline Template of the box in .ai and .jpg
9)Vectors for the different uses of the helmets
Your design should reflect our brand and communicate the product's value while standing out on retail shelves.
The winner will be selected based on creativity, brand alignment, and overall design aesthetics.
We look forward to seeing your creative concepts.
Target Market(s)
Industrial and Retail
Industry/Entity Type
Welding, Retail, Hardware
Colors
Designer to choose colors to be used in the design.
Look and feel
Each slider illustrates characteristics of the customer's brand and the style your logo design should communicate.

```html
<!DOCTYPE html>
<html lang="en">
<head>
<meta charset="utf-8">
<title>Brontal Welding Helmet – Retail Box and Sticker</title>
<link rel="stylesheet" href="https://fonts.googleapis.com/css2?family=Montserrat:wght@600;700;800;900&family=Roboto+Condensed:wght@400&family=Saira+Condensed:ital,wght@0,700;1,800&display=swap">
<style>
  :root {
    --ink: #0c0a10;
    --purple-deep: #1c0f3a;
    --purple-mid: #3a1b6b;
    --purple: #5b2a8f;
    --purple-bright: #7b3fc4;
    --tile: #5b2d95;
    --magenta: #8a2a9e;
    --white: #ffffff;
    --backdrop: #f3f3f5;
  }
  * { box-sizing: border-box; margin: 0; padding: 0; }
  html, body { width: 820px; height: 1200px; overflow: hidden; }
  body { background: var(--backdrop); position: relative; font-family: "Montserrat", sans-serif; }

  /* Outlined lettering: a stroked layer under a filled layer hides inner contour overlaps */
  .outlined { position: relative; display: inline-block; }
  .outlined-stroke { display: block; color: var(--white); -webkit-text-stroke: var(--stroke, 4px) var(--white); }
  .outlined-fill { position: absolute; left: 0; top: 0; display: block; color: var(--fill, var(--ink)); }

  /* ---------- Box front ---------- */
  .box-front {
    position: absolute; left: 150px; top: 30px; width: 520px; height: 725px;
    overflow: hidden; box-shadow: 0 10px 30px rgba(0,0,0,.18);
  }
  .box-header { position: absolute; inset: 0 0 auto 0; height: 185px; background: var(--ink); }
  .brand { position: absolute; left: 40px; top: 95px; display: flex; align-items: center; gap: 10px; }
  .brand-dot { width: 14px; height: 14px; border-radius: 50%; background: var(--purple-bright); }
  .brand-name {
    font-weight: 800; font-size: 22px; line-height: 1.1;
    color: var(--white); letter-spacing: 1px; text-transform: uppercase;
  }
  .solutions { position: absolute; right: 22px; top: 58px; text-align: right; }
  .solutions-rule { width: 100px; height: 3px; background: var(--magenta); margin-left: auto; margin-bottom: 6px; }
  .solutions-title {
    font-family: "Saira Condensed", sans-serif; font-weight: 700; font-size: 19px; line-height: 1;
    text-transform: uppercase; --stroke: 2px; --fill: var(--ink);
  }
  .process-list { display: flex; gap: 10px; margin-top: 12px; justify-content: flex-end; list-style: none; }
  .process { display: flex; flex-direction: column; align-items: center; gap: 3px; width: 34px; }
  .process-ring { width: 30px; height: 30px; border-radius: 50%; border: 2px solid var(--white); }
  .process-label {
    font-family: "Saira Condensed", sans-serif; font-weight: 700; font-size: 10px; color: var(--white); text-transform: uppercase;
  }

  .box-feature { position: absolute; left: 0; top: 185px; width: 560px; height: 320px; transform: scale(.93); transform-origin: 0 0; }

  .tagline-band {
    position: absolute; left: 0; right: 0; top: 482px; height: 28px; background: var(--white);
    display: flex; align-items: center; justify-content: center;
    font-weight: 700; font-size: 16px; color: var(--purple-mid); letter-spacing: .5px;
  }
  .headline-dark { position: absolute; left: 0; right: 0; top: 510px; height: 110px; background: var(--ink); }
  .headline-light { position: absolute; left: 0; right: 0; top: 620px; height: 105px; background: var(--purple); }
  .headline { position: absolute; left: 0; right: 0; text-align: center; font-weight: 900; text-transform: uppercase; line-height: 1; }
  .headline--ultimate { top: 522px; font-size: 40px; color: var(--magenta); left: 50px; }
  .headline--welding { top: 560px; font-size: 62px; color: var(--white); left: 40px; }
  .headline--helmet { top: 634px; font-size: 80px; left: 40px; letter-spacing: 2px; --stroke: 5px; --fill: var(--purple); }

  /* ---------- Feature panel (shared) ---------- */
  .feature-panel {
    position: relative; width: 560px; height: 320px; overflow: hidden;
    background: linear-gradient(160deg, var(--purple-deep) 0%, var(--purple-mid) 50%, var(--purple) 100%);
  }
  .product-name {
    position: absolute; left: 50px; top: 14px;
    font-family: "Saira Condensed", sans-serif; font-style: italic; font-weight: 800; font-size: 70px; line-height: 1;
    text-transform: uppercase; letter-spacing: 1px; --stroke: 4px; --fill: var(--purple-bright);
  }
  .features {
    position: absolute; left: 55px; top: 100px; width: 215px; height: 205px; list-style: none;
    border: 1.5px dashed rgba(255,255,255,.75); border-radius: 12px; padding: 10px 14px;
  }
  .feature { display: flex; align-items: center; gap: 14px; height: 46px; position: relative; }
  .feature + .feature::before {
    content: ""; position: absolute; left: 58px; right: -2px; top: 0; height: 1.5px; background: var(--white);
  }
  .feature-icon {
    width: 44px; height: 44px; flex: none; border-radius: 6px; background: var(--tile);
    display: flex; align-items: center; justify-content: center;
  }
  .feature-icon svg { width: 32px; height: 32px; }
  .feature-title { font-weight: 700; font-size: 14px; color: var(--white); line-height: 1.1; text-transform: uppercase; letter-spacing: .5px; }
  .feature-text { font-family: "Roboto Condensed", sans-serif; font-size: 10.5px; color: var(--white); line-height: 1.25; }
  .helmet-photo {
    position: absolute; left: 318px; top: 16px; width: 225px; height: 292px;
    border-radius: 48% 44% 38% 42% / 42% 40% 50% 50%;
    background: radial-gradient(ellipse at 40% 30%, #3a3a42 0%, #111114 55%, #050507 100%);
    box-shadow: 0 0 0 2px var(--magenta);
  }

  /* ---------- Sticker ---------- */
  .sticker {
    position: absolute; left: 130px; top: 795px; width: 560px; height: 352px;
    box-shadow: 0 8px 24px rgba(0,0,0,.16); overflow: hidden;
  }
  .sticker-tagline {
    position: absolute; left: 0; right: 0; top: 320px; height: 25px; background: var(--white);
    display: flex; align-items: center; justify-content: center;
    font-weight: 700; font-size: 17px; color: var(--purple-mid); letter-spacing: .5px;
  }
  .sticker-base { position: absolute; left: 0; right: 0; top: 345px; height: 7px; background: var(--purple); }
</style>
</head>
<body>

<svg width="0" height="0" style="position:absolute">
  <defs>
    <symbol id="icon-delay" viewBox="0 0 32 32"><circle cx="17" cy="17" r="10" fill="none" stroke="#fff" stroke-width="2.5"/><path d="M17 11v6l4 3" fill="none" stroke="#fff" stroke-width="2.5" stroke-linecap="round"/><path d="M4 14h5M3 18h5M5 22h4" stroke="#fff" stroke-width="2" stroke-linecap="round"/></symbol>
    <symbol id="icon-sensitivity" viewBox="0 0 32 32"><path d="M6 20a10 10 0 0 1 20 0" fill="none" stroke="#fff" stroke-width="2.5"/><path d="M16 9c-4 6-6 8.5-6 11.5a6 6 0 0 0 12 0C22 17.5 20 15 16 9z" fill="#fff"/></symbol>
    <symbol id="icon-grind" viewBox="0 0 32 32"><path d="M5 9h22M5 16h22M5 23h22" stroke="#fff" stroke-width="2.5" stroke-linecap="round"/><rect x="10" y="6" width="4" height="6" rx="1" fill="#fff"/><rect x="19" y="13" width="4" height="6" rx="1" fill="#fff"/><rect x="13" y="20" width="4" height="6" rx="1" fill="#fff"/></symbol>
    <symbol id="icon-test" viewBox="0 0 32 32"><circle cx="11" cy="11" r="5" fill="none" stroke="#fff" stroke-width="3" stroke-dasharray="3 2"/><circle cx="20" cy="21" r="7" fill="none" stroke="#fff" stroke-width="2.5" stroke-dasharray="3.5 2"/><circle cx="20" cy="21" r="3" fill="none" stroke="#fff" stroke-width="2"/><circle cx="7" cy="24" r="3" fill="none" stroke="#fff" stroke-width="2"/></symbol>
  </defs>
</svg>

<section class="box-front" aria-label="Brontal retail box, front panel">
  <header class="box-header">
    <div class="brand">
      <span class="brand-dot"></span>
      <span class="brand-name">Kordan<br>Weldworks</span>
    </div>
    <div class="solutions">
      <div class="solutions-rule"></div>
      <p class="solutions-title outlined"><span class="outlined-stroke" aria-hidden="true">Welding &amp;<br>Cutting Solutions</span><span class="outlined-fill">Welding &amp;<br>Cutting Solutions</span></p>
      <ul class="process-list">
        <li class="process"><span class="process-ring"></span><span class="process-label">MIG</span></li>
        <li class="process"><span class="process-ring"></span><span class="process-label">TIG</span></li>
        <li class="process"><span class="process-ring"></span><span class="process-label">Stick</span></li>
        <li class="process"><span class="process-ring"></span><span class="process-label">Plasma</span></li>
        <li class="process"><span class="process-ring"></span><span class="process-label">Grind</span></li>
      </ul>
    </div>
  </header>

  <div class="box-feature">
    <div class="feature-panel">
      <h1 class="product-name outlined"><span class="outlined-stroke" aria-hidden="true">Brontal</span><span class="outlined-fill">Brontal</span></h1>
      <ul class="features">
        <li class="feature"><span class="feature-icon"><svg><use href="#icon-delay"/></svg></span><div><p class="feature-title">Delay</p><p class="feature-text">Simple shift fast/mid/slow<br>from 0.1~0.8s</p></div></li>
        <li class="feature"><span class="feature-icon"><svg><use href="#icon-sensitivity"/></svg></span><div><p class="feature-title">Sensitivity</p><p class="feature-text">Swithches from light to dark<br>in just 1/25000 sec</p></div></li>
        <li class="feature"><span class="feature-icon"><svg><use href="#icon-grind"/></svg></span><div><p class="feature-title">Grind</p><p class="feature-text">Easy outside control</p></div></li>
        <li class="feature"><span class="feature-icon"><svg><use href="#icon-test"/></svg></span><div><p class="feature-title">Test</p><p class="feature-text">Self-testing and<br>low battery notice</p></div></li>
      </ul>
      <div class="helmet-photo" role="img" aria-label="Product photo of the black auto-darkening Brontal welding helmet with violet lens"></div>
    </div>
  </div>

  <div class="tagline-band">The choice of experts.</div>
  <div class="headline-dark"></div>
  <div class="headline-light"></div>
  <p class="headline headline--ultimate">Ultimate</p>
  <p class="headline headline--welding">Welding</p>
  <p class="headline headline--helmet"><span class="outlined"><span class="outlined-stroke" aria-hidden="true">Helmet</span><span class="outlined-fill">Helmet</span></span></p>
</section>

<section class="sticker" aria-label="Brontal product sticker">
  <div class="feature-panel">
    <h2 class="product-name outlined"><span class="outlined-stroke" aria-hidden="true">Brontal</span><span class="outlined-fill">Brontal</span></h2>
    <ul class="features">
      <li class="feature"><span class="feature-icon"><svg><use href="#icon-delay"/></svg></span><div><p class="feature-title">Delay</p><p class="feature-text">Simple shift fast/mid/slow<br>from 0.1~0.8s</p></div></li>
      <li class="feature"><span class="feature-icon"><svg><use href="#icon-sensitivity"/></svg></span><div><p class="feature-title">Sensitivity</p><p class="feature-text">Swithches from light to dark<br>in just 1/25000 sec</p></div></li>
      <li class="feature"><span class="feature-icon"><svg><use href="#icon-grind"/></svg></span><div><p class="feature-title">Grind</p><p class="feature-text">Easy outside control</p></div></li>
      <li class="feature"><span class="feature-icon"><svg><use href="#icon-test"/></svg></span><div><p class="feature-title">Test</p><p class="feature-text">Self-testing and<br>low battery notice</p></div></li>
    </ul>
    <div class="helmet-photo" role="img" aria-label="Product photo of the black auto-darkening Brontal welding helmet with violet lens"></div>
  </div>
  <div class="sticker-tagline">The choice of experts.</div>
  <div class="sticker-base"></div>
</section>

</body>
</html>
```